RW Stewardship real estate management company needs presentation folder to hand clients

looking for a folder with pockets that represent my real estate management company when i hand to client reports or promotional material. I only do resedential real estate. I want classy and professional - pictures or additioal graphixs are fine

when a client open i will usally insert text and reports about my business
also on the inside flap is usally place for my business card i will upload a picture so the theme can be constant

Target Market(s)

my existing real estate cleints
and i will use when i am soliciting new business

Industry/Entity Type

Real Estate

Font styles to use
Serif

Requirements
Must have
• must have logo
• must give appearance of professionalism and maturity
• have basic company info tel# ,address
• id like viewer to know I manage real estate - focus on residential small to large apartment buildings
• not strip malls, not giganic complexes - im a mid size company
• logo is black but i welcome color as u see fit
Nice to have
• maybe pictures
• my slogan - " we will manage your building like its our own "
• focus on professioanl, safe, trust worthy
• type style should be clear and readable - but im open to sugestions

```html
<!DOCTYPE html>
<html lang="en">
<head>
<meta charset="utf-8">
<title>RW Stewardship — Presentation Folder</title>
<link href="https://fonts.googleapis.com/css2?family=Montserrat:wght@400;500;600;700;800&family=Source+Sans+3:wght@400;600&display=swap" rel="stylesheet">
<style>
  :root {
    --paper: #ffffff;
    --ink: #111111;
    --sky-top: #8fcdea;
    --sky-low: #d7f0f7;
    --facade: #f1f3f4;
    --facade-mid: #b9c2ca;
    --facade-dark: #2e3338;
    --overlay: rgba(12, 12, 14, 0.78);
    --pocket: #eceff0;
    --rule: #ffffff;
    --crop: #d0409a;
  }
  * { margin: 0; padding: 0; box-sizing: border-box; }
  html, body { width: 1200px; height: 1075px; overflow: hidden; background: var(--paper); }
  .folder { position: relative; width: 1200px; height: 1075px; }

  .cover { position: absolute; left: 108px; top: 67px; width: 1028px; height: 716px; overflow: hidden; }
  .cover-photo {
    position: absolute; inset: 0;
    background:
      linear-gradient(180deg, var(--sky-top) 0%, var(--sky-low) 22%, rgba(215,240,247,0) 34%),
      radial-gradient(ellipse 38% 48% at 24% 60%, rgba(46,51,56,0.75) 0%, rgba(46,51,56,0) 100%),
      radial-gradient(ellipse 30% 40% at 88% 45%, rgba(255,255,255,0.9) 0%, rgba(255,255,255,0) 100%),
      linear-gradient(90deg, var(--facade-mid) 0%, var(--facade) 8%, #d9dde0 30%, var(--facade) 55%, #e4e7e9 78%, #c8ced3 100%);
  }
  .cover-shade { position: absolute; inset: 0; background: linear-gradient(180deg, rgba(0,0,0,0) 45%, rgba(46,51,56,0.55) 75%, rgba(20,22,25,0.85) 100%); }
  .cover-band { position: absolute; inset: 0; }

  .contact { position: absolute; left: 119px; top: 38px; font-family: "Source Sans 3", sans-serif; font-size: 15.5px; line-height: 19.5px; color: var(--ink); font-style: normal; }

  .brand { position: absolute; right: 48px; top: 92px; display: flex; align-items: center; gap: 8px; font-family: "Montserrat", sans-serif; font-weight: 700; font-size: 17px; color: var(--ink); letter-spacing: 0.3px; }
  .brand-square { width: 14px; height: 14px; background: var(--ink); }

  .slogan { position: absolute; left: 599px; top: 519px; width: 341px; color: #fff; font-family: "Montserrat", sans-serif; text-align: center; white-space: nowrap; }
  .slogan-rule { height: 1px; background: var(--rule); }
  .slogan-lead { font-weight: 500; font-size: 23px; line-height: 34px; letter-spacing: 0.4px; }
  .slogan-main { font-weight: 800; font-size: 35px; line-height: 44px; margin-top: 4px; letter-spacing: -0.3px; }
  .slogan-tail { font-weight: 500; font-size: 30px; line-height: 38px; }

  .pocket { position: absolute; left: 0; top: 0; width: 1200px; height: 1075px; }

  .card { position: absolute; left: 232px; top: 833px; width: 225px; height: 135px; background: var(--ink); }
  .card-face { position: absolute; left: 12px; top: 12px; width: 201px; height: 111px; background: #fff; }
  .card-frame { position: absolute; inset: 3px; border: 1px solid var(--ink); }
  .card-brand { position: absolute; left: 9px; top: 40px; display: flex; align-items: center; gap: 3px; font-family: "Montserrat", sans-serif; font-weight: 700; font-size: 7px; color: var(--ink); white-space: nowrap; }
  .card-brand i { width: 6px; height: 6px; background: var(--ink); display: block; }
  .card-divider { position: absolute; left: 96px; top: 24px; width: 1px; height: 53px; background: var(--ink); }
  .card-details { position: absolute; right: 8px; top: 24px; text-align: right; font-family: "Montserrat", sans-serif; color: var(--ink); }
  .card-name { font-weight: 800; font-size: 11.5px; line-height: 13px; letter-spacing: -0.3px; }
  .card-title { font-size: 5px; line-height: 8px; font-weight: 500; }
  .card-line { font-size: 5px; line-height: 6.6px; }
  .card-address { font-size: 3.2px; line-height: 6px; }
  .card-slogan { position: absolute; left: 8px; right: 8px; top: 93px; display: flex; align-items: center; gap: 5px; font-family: "Montserrat", sans-serif; font-size: 4.4px; font-weight: 600; color: var(--ink); white-space: nowrap; }
  .card-slogan span.rule { flex: 1; height: 0.5px; background: #777; }

  .crop { position: absolute; left: 0; top: 0; width: 1200px; height: 1075px; pointer-events: none; }
</style>
</head>
<body>
<div class="folder">
  <section class="cover">
    <div class="cover-photo" role="img" aria-label="Photograph of a modern white and dark-framed residential apartment building against a blue sky, with palm plants in front"></div>
    <div class="cover-shade"></div>
    <svg class="cover-band" width="1028" height="716" viewBox="0 0 1028 716">
      <polygon points="284,500 659,358 1028,500 1028,716 284,716" fill="var(--overlay)"/>
    </svg>

    <address class="contact">
      phone: 555-210-4470<br>
      email: office@rwstewardship.com<br>
      cell: 555-381-9026
    </address>

    <div class="brand"><span class="brand-square"></span>RW Stewardship</div>

    <div class="slogan">
      <div class="slogan-rule"></div>
      <p class="slogan-lead">WE WILL MANAGE</p>
      <div class="slogan-rule"></div>
      <p class="slogan-main">YOUR BUILDING</p>
      <p class="slogan-tail">LIKE IT IS OUR OWN</p>
    </div>
  </section>

  <svg class="pocket" width="1200" height="1075" viewBox="0 0 1200 1075">
    <path d="M108 783 L600 783 Q608 783 608 791 L608 1010 Q608 1018 600 1018 L108 1018 L73 1010 L73 812 Z" fill="var(--pocket)"/>
  </svg>

  <div class="card">
    <div class="card-face">
      <div class="card-frame"></div>
      <div class="card-brand"><i></i>RW Stewardship</div>
      <div class="card-divider"></div>
      <div class="card-details">
        <p class="card-name">Daniel Marsh</p>
        <p class="card-title">MASTER BUILDING MANAGER</p>
        <p class="card-line">office tel 555-210-4470</p>
        <p class="card-line">email office@rwstewardship.com</p>
        <p class="card-line">cell 555-381-9026</p>
        <p class="card-address">22 ALDER COURT SUITE 4 RIVERTON NY 10000</p>
      </div>
      <div class="card-slogan"><span class="rule"></span>WE WILL MANAGE YOUR BUILDING LIKE IT IS OUR OWN<span class="rule"></span></div>
    </div>
  </div>

  <svg class="crop" width="1200" height="1075" viewBox="0 0 1200 1075">
    <line x1="227" y1="876" x2="274" y2="829" stroke="var(--crop)" stroke-width="0.8"/>
    <line x1="420" y1="975" x2="468" y2="927" stroke="var(--crop)" stroke-width="0.8"/>
  </svg>
</div>
</body>
</html>
```